Stationary for a Legal Support Company
Brimvale Courier & Records, Inc.
Stationary for a Legal Support Company - Marketing
Creative Brief
Professional
Rupert J Olwen
PO Box 712 4175 Marrow Ln Twinsburg OH 44087
tkorvel@brimcr.com
www.brimcr.com
Generic USB flash and CD/DVD layout also appreciated.
Back of the card can include the logo or logo/text.
tkorvel tkorvel
Thank you all for your submissions. I believe I have sent some comments to everyone who has entered a submission. If you did not receive a comment from me, please let me know.

```html
<!DOCTYPE html>
<html lang="en">
<head>
<meta charset="utf-8">
<title>Brimvale Courier &amp; Records – Business Card</title>
<link rel="stylesheet" href="https://fonts.googleapis.com/css2?family=Open+Sans:wght@400;600&display=swap">
<style>
  :root {
    --page-bg: #dcdbd7;
    --card-bg: #fbfbfa;
    --brand-blue: #2d5c9f;
    --text-ink: #3a3a3a;
    --text-on-blue: #ffffff;
  }
  * { box-sizing: border-box; margin: 0; padding: 0; }
  html, body {
    width: 1200px; height: 940px; overflow: hidden;
    background: var(--page-bg);
    font-family: "Open Sans", Arial, sans-serif;
  }
  .stage {
    width: 1200px; height: 940px;
    display: flex; align-items: center; justify-content: center;
  }
  .business-card {
    position: relative;
    width: 880px; height: 503px;
    background: var(--card-bg);
    border-radius: 34px;
    box-shadow: 0 10px 30px rgba(0,0,0,0.18);
    overflow: hidden;
  }
  .brand-mark {
    position: absolute; left: 64px; top: 70px;
    display: flex; align-items: center; gap: 20px;
  }
  .brand-dot {
    width: 58px; height: 58px; border-radius: 50%;
    border: 3px solid var(--brand-blue);
  }
  .brand-name {
    color: var(--brand-blue);
    font-weight: 400;
    font-size: 26px;
    letter-spacing: 2px;
    text-transform: uppercase;
    line-height: 1.2;
  }
  .band-graphic {
    position: absolute; left: 0; top: 170px;
    width: 880px; height: 170px;
  }
  .identity {
    position: absolute; left: 64px; top: 208px;
    color: var(--text-on-blue);
  }
  .person-name {
    font-size: 40px; font-weight: 400;
    letter-spacing: 2px; text-transform: uppercase;
    line-height: 1.1;
  }
  .person-title {
    font-size: 24px; font-weight: 400; margin-top: 6px;
  }
  .contact-list {
    position: absolute; left: 64px; top: 362px;
    list-style: none;
    color: var(--text-ink);
    font-size: 19px; line-height: 1.5;
  }
</style>
</head>
<body>
<main class="stage">
  <article class="business-card">
    <div class="brand-mark">
      <span class="brand-dot"></span>
      <span class="brand-name">Brimvale Courier<br>&amp; Records</span>
    </div>

    <svg class="band-graphic" viewBox="0 0 880 170" aria-hidden="true">
      <rect x="0" y="0" width="880" height="8" fill="var(--brand-blue)"/>
      <rect x="0" y="18" width="880" height="134" fill="var(--brand-blue)"/>
      <rect x="0" y="162" width="880" height="8" fill="var(--brand-blue)"/>
    </svg>

    <div class="identity">
      <h1 class="person-name">Rupert J Olwen</h1>
      <p class="person-title">Managing Director</p>
    </div>

    <ul class="contact-list">
      <li>PO Box 712 4175 Marrow Ln Twinsburg OH 44087</li>
      <li>012 555 01934</li>
      <li>tkorvel@brimcr.com</li>
      <li>www.brimcr.com</li>
    </ul>
  </article>
</main>
</body>
</html>
```